Pellano Growth Brochure Design Project

- Who we are?
Pellano Growth is New Internet Marketing Company Based in China.

It is our aim to provide Chinese clients with the means to internationally market their product, via the Internet.

Our primary products are Outsourced Design ( Thanks to Artwell hub and the amazing designers who use it), SEO and Virtual Hosting.

- Project Brief
Design a vibrant and fresh brochure that introduces the fundamentals of SEO. There is no restriction to the number of pages, however all the info I have included in this brief must be included.

- Colour Palette
Please see link or download the Vantoria Swatch Exchange File or follow the link below
http://hues.vantoria-sample.com/#themes/search?term=4817350

Logo updated - grey background removed

Various file formats added for logo and brochure content

Brochure zip file add containing logo in different formats.

Vantoria color scheme file added

The general corporate colors are:

Base Color: CMYK :0, 60, 80, 0  Hex: FF6633
Dark Orange: CMYK: 0, 72, 96, 30 Hex: B23308
Light Orange: CMYK 0, 42, 56, 0 Hex: FF9571
Grey: CMYK 0, 0, 0, 48 Hex: 858585
Light Grey: CMYK 0, 0, 0, 26 Hex: BDBDBD

Please note that I'm happy for other colors to be included, however I would like these the corporate branding colors to be clearly present through the brochure.

Hi All

First place payment has increased to $600 - Looking to see some creative designs!

Hi All

Reason: I have increase the budget and extend the deadline as I need to see more design.

I have attached a zip file that contains example brochures I like.

We are not keen on the table data its a little plain. We have create an info-graphic to replace one of the table and would like to see it included in the design.

Reason: A few designers have asked for this extension and I would like to see additional designs. Thanks Marek

Target Market(s)

- Our Target Audience is..
It is small to medium businesses looking to reach out to the international market.
Our clients still very much operate on a face to face level in business and are new to the concept of Internet marketing

However this must look professional, Marketable and Clean, with the power of connecting people globally, through SEO and design to be reflected visually in the brochure.

Industry/Entity Type

Internet

Requirements
Must have
• One or more of the FACTS that I have highlighted need to stand out on each page. These FACTS can be found the document attached to this brief and are under the section titled 'Did You Know!'. Not every fact in this section needs to be highlighted in the brochure, but each page needs to have at least, one or more fact that stands out, soemwhere on the page.
See attached document, under the heading 'Did you Know!' and use one or two of these facts to spruce up the pages!

One image/ per page or per two pages MUST be included!

- Provide stock photos and please send us a message with the additional cost of these with your submission

The Table data, that I have included in the attachment must be included in the body of the pages - BUT the table format is not necessary and you can place the information in the body like plain text.

The brochure size should be a little larger than A4.

Please design the back page, like a pocket to hold paper and other material in it that I include with this brochure.

```html
<!DOCTYPE html>
<html lang="en">
<head>
<meta charset="utf-8">
<title>Pellano Growth – SEO</title>
<link href="https://fonts.googleapis.com/css2?family=Source+Sans+3:wght@400;600&display=swap" rel="stylesheet">
<style>
  :root {
    --brand-orange: #F26127;
    --table-orange: #DE834D;
    --band-grey: #EDEDEF;
    --cell-grey: #EFEFF1;
    --ink: #262626;
    --cell-ink: #3a3a3a;
    --white: #ffffff;
  }
  * { margin: 0; padding: 0; box-sizing: border-box; }
  html, body { width: 900px; height: 1200px; overflow: hidden; background: var(--white); }
  body { font-family: "Source Sans 3", "Myriad Pro", sans-serif; color: var(--ink); }
  .page { position: relative; width: 900px; height: 1200px; }

  .page-header { position: absolute; left: 6px; top: 14px; width: 886px; height: 67px; }
  .page-header svg { display: block; }
  .page-title {
    position: absolute; left: 21px; top: 4px;
    font-size: 42px; font-weight: 400; color: var(--white); letter-spacing: 0.5px;
  }

  .body-copy {
    position: absolute; left: 27px; width: 842px;
    font-size: 16.2px; line-height: 30.5px; text-align: justify;
  }
  .body-copy p + p { margin-top: 11px; }
  .intro { top: 108px; }

  .question-band {
    position: absolute; left: 6px; top: 337px; width: 884px; height: 115px;
    background: var(--band-grey);
  }
  .question-band h3 {
    position: absolute; left: 21px; top: 8px;
    font-size: 16.2px; font-weight: 400;
  }
  .question-band p {
    position: absolute; left: 21px; top: 47px; width: 842px;
    font-size: 16.2px; line-height: 30.5px; text-align: justify;
  }

  .section-heading { position: absolute; left: 27px; top: 464px; font-size: 27px; font-weight: 400; }
  .seo-copy { top: 510px; }
  .seo-copy p + p { margin-top: 25px; }

  .comparison {
    position: absolute; left: 27px; top: 829px; width: 844px;
    display: grid;
    grid-template-columns: 161px 73px 263px 75px 264px;
    grid-template-rows: 64px 63px 90px 91px;
    column-gap: 3px; row-gap: 4px;
    font-size: 10.4px; line-height: 16.5px; color: var(--cell-ink);
  }
  .comparison .head {
    background: var(--table-orange); color: var(--white);
    font-size: 15px; display: flex; align-items: center; justify-content: center;
  }
  .comparison .head.blank { }
  .comparison .head.span { grid-column: span 2; }
  .comparison .cell { background: var(--cell-grey); padding: 12px 10px 0 13px; }
  .comparison .cell.detail { text-align: justify; padding-right: 14px; }
  .comparison .cell.rating { padding-left: 10px; }
  .comparison .cell.detail p + p { margin-top: 11px; }
</style>
</head>
<body>
<div class="page">
  <header class="page-header">
    <svg width="886" height="67" viewBox="0 0 886 67" aria-hidden="true">
      <rect x="0" y="0" width="886" height="67" fill="var(--band-grey)"/>
      <polygon points="0,0 138,0 204,67 0,67" fill="var(--brand-orange)"/>
      <polygon points="138,0 148,0 214,67 204,67" fill="var(--white)"/>
    </svg>
    <h1 class="page-title">SEO</h1>
  </header>

  <section class="body-copy intro">
    <p>Pellano Growth doesn’t believe that traditional marketing is finished and out of the fight, but it does believe that Traditional Marketing without SEO is. However, imagine hiring a sales man who works 24 hours a day, 7 days a week, who can deal with hundreds and thousands of customers at the same time and still personalize the response to consumer. Sounds amazing, right?&nbsp; That’s not all - he wants to work for very little money. Who is this sales man?</p>
    <p>The Sales man is actually all of the international search engines. Search engines deal with over 120 billion plus searches every month.</p>
  </section>

  <aside class="question-band">
    <h3>How do I Turn a Search engine into my personal sales man?</h3>
    <p>People trust search engines so if the search engine suggests say this sit is the best people trust it and visit the site. So how do I get a search engine to suggest my site?</p>
  </aside>

  <h2 class="section-heading">SEO</h2>
  <section class="body-copy seo-copy">
    <p>To understand SEO&nbsp; you have to understand search engines. Search engines visit more than 40 billion pages a day and add them to their databases of pages. During this process it gives each page a page rank. This rank is based on a very complex equation containing many factors.&nbsp; They also create lists of ‘keywords’ that it associates to the website and it gathers other information ie link to other sites, amount of time a user spends on a page and much more.When a user searches for a word, search engines use all of this data to calculate the order it displays the results. However this is not the end of it search engines also change the results based on how popular a page or site is, so the more popular you are the more the visits you get.</p>
    <p>SEO is about understanding this process and ensuring that you site is popular aand ticks the right boxes. So let the experts at Pellano Growth get your website to the front page - all you have to do is sit back and enjoy the rewards.</p>
  </section>

  <div class="comparison" role="table">
    <div class="head blank"></div>
    <div class="head span">Online Marketing and SEO</div>
    <div class="head span">Traditional???</div>

    <div class="cell">Cost</div>
    <div class="cell rating">Low Cost</div>
    <div class="cell detail">SEO cost are lower than traditional marketing cost and reach an international audience</div>
    <div class="cell rating">High Cost</div>
    <div class="cell detail"><p>Human Resources cost a lot of money.</p><p>Media coverage costs a lot of money</p></div>

    <div class="cell">Return On Investment</div>
    <div class="cell rating">Low Risk/High Return</div>
    <div class="cell detail">Due to its low implementation costs, SEO has a very high return on investment (ROI). This reduces the risk you need to take to maintain or increase profits</div>
    <div class="cell rating">High Risk /Low To Medium Return</div>
    <div class="cell detail">Traditional marketing involves high up-front costs that may never return your original investment.</div>

    <div class="cell">Availability to Business</div>
    <div class="cell rating">Any size business</div>
    <div class="cell detail">Due to low cost and high return SEO is available to any business</div>
    <div class="cell rating">Medium to large corporations</div>
    <div class="cell detail">Due to media costs it is virtual impossible to get wide national coverage for a small company</div>
  </div>
</div>
</body>
</html>
```